Progressive business consultancy seeking innovative and clever powerpoint design

Were looking for a PowerPoint design for our Melbourne based business consulting company, Vantora.

About Us:
Based in Melbourne, Australia, Vantora is a management consulting organisation that partners with their clients to lead the execution of strategic process and system improvement initiatives.

Vantora offers business advisory services in Project Management, Business Process Management, Change Management, Business Analysis and Business Intelligence. Vantora combines hands on delivery with coaching in best practice methodologies and approaches to build our clients capabilities ensuring their ongoing success in project implementations.

Vantora has extensive experience across a wide range of industries. We specialise in assisting organisations across the accounting, legal, financial services and health sectors.

Our core purpose is to help businesses in the middle market navigate transformational change through clear and focused execution and enablement.

www.vantora.com.au
@vantora_hq

What we're looking for:
A PowerPoint template consisting of:
- a front/cover page with hero image (attached)
- a contents page
- a divider page (for different segments of the slide deck)
- a standard PowerPoint content page
- a blank PowerPoint page. (still Vantora themed)

The Vantora colours are white and blue (RGB:0/86/162 and
CMYK 97/73/4/0)

All slides should have the Vantora logo (attached) and a professional, almost corporate, (but not boring) theme that is consistent across all slides. The design should reflect our focus on the "e" in vantora, which is what we're really about - "e"xecution and "e"nablement of change.

I've attached a PNG file of our word template which shows the focus on the "e" as a watermark on the document as well as the font files if required.

Let me know if you need any further information or design specifics.

Thanks,

Marjorie
(on behalf of Desmond)
Updates

Project Deadline Extended
Reason: Hi Designers, We have received some really great designs. Thanks for taking the time to make your submissions. We have decided to extend the deadline as we need some more time to review and consult other colleagues on the great submissions we have received. We are also hoping we might get some additional submissions over the weekend. We would also like enough time to provide feedback on all the submissions received. Thanks for helping us out with some really creative work. Desmond @vantora_hq

Project Deadline Extended
Reason: Hi designers, thanks for taking the time to submit your designs. We have some really great submissions. We are going to have to extend our deadline again as we just haven't had the chance to review and provide feedback on all the designs. We will be closing this project off on Tuesday March 17. Thanks Desmond @vantora_hq

Target Market(s)

C-Level executives (CEO,COO,CIO) at professional services firms (Accounting and Legal), not for profit organisations and financial services firms.

Industry/Entity Type

Management Consulting

Font styles to use
Serif
Other font styles liked:
• Calibri or attached fonts

Requirements
Must have
• A PowerPoint template consisting of:
• 1) a front/cover page with hero image (attached)
• 2) a contents page
• 3) a divider page (for different segments of the slide deck)
• 4) a standard PowerPoint content page
• 5) a blank PowerPoint page. (still Vantora themed)
• 6) Two content
• 7) Comparison
• 8) Table
• 9) Picture column
• 10) Chevron
• The Vantora colours are white and blue (RGB:0/86/162 and
• CMYK 97/73/4/0)

```html
<!DOCTYPE html>
<html lang="en">
<head>
<meta charset="utf-8">
<title>Vantora Presentation Template</title>
<link rel="stylesheet" href="https://fonts.googleapis.com/css2?family=PT+Sans:ital,wght@0,400;0,700;1,400&family=PT+Sans+Narrow:wght@400;700&display=swap">
<style>
  :root {
    --stage: #1c1e21;
    --brand-blue: #0056a2;
    --band-top: #0d5d9e;
    --band-bottom: #0a3f78;
    --title-blue: #0d3b73;
    --body-ink: #1d2a3a;
    --tick-ink: #2b3a4c;
    --paper-top: #ffffff;
    --paper-bottom: #d9eef8;
    --bar-top: #1a68b8;
    --bar-bottom: #0a3d7a;
    --bar-edge: #0a1a2c;
    --chip: #262a30;
    --chip-text: #e8edf3;
    --white: #ffffff;
  }
  * { margin: 0; padding: 0; box-sizing: border-box; }
  html, body { width: 1200px; height: 900px; overflow: hidden; background: var(--stage); }
  .canvas { position: relative; width: 1200px; height: 900px; background: var(--stage); }

  .slide {
    position: absolute; width: 585px; height: 437px; overflow: hidden;
    background: linear-gradient(180deg, var(--paper-top) 0%, #eaf7fc 40%, var(--paper-bottom) 100%);
    font-family: "PT Sans Narrow", "Arial Narrow", sans-serif;
  }
  .slide--cover    { left: 10px;  top: 8px; }
  .slide--outline  { left: 605px; top: 8px; }
  .slide--about    { left: 10px;  top: 455px; }
  .slide--services { left: 605px; top: 455px; }

  /* footer bar */
  .footer-bar {
    position: absolute; left: 0; right: 0; bottom: 0; height: 43px;
    background: linear-gradient(180deg, var(--bar-top), var(--bar-bottom));
    border-top: 3px solid var(--bar-edge);
    display: flex; align-items: center; padding: 0 14px;
  }
  .slide-number {
    width: 30px; height: 24px; background: var(--chip); color: var(--chip-text);
    font-family: "PT Sans", sans-serif; font-size: 16px; line-height: 24px; text-align: center;
    border-radius: 2px;
  }
  .footer-text {
    margin-left: 18px; color: var(--white); font-family: "PT Sans", sans-serif;
    font-style: italic; font-size: 13.5px; flex: 1;
  }
  .footer-text--date { margin-left: 48px; font-size: 14px; }
  .nav { display: flex; gap: 8px; }
  .nav-button {
    height: 26px; background: linear-gradient(180deg, #3a3f46, #1f2226); color: var(--chip-text);
    font-family: "PT Sans", sans-serif; font-size: 12.5px; line-height: 26px; text-align: center;
  }
  .nav-button--back { width: 48px; padding-left: 6px; clip-path: polygon(10px 0, 100% 0, 100% 100%, 10px 100%, 0 50%); }
  .nav-button--next { width: 48px; padding-right: 6px; clip-path: polygon(0 0, calc(100% - 10px) 0, 100% 50%, calc(100% - 10px) 100%, 0 100%); }
  .nav-button--start { width: 44px; border-radius: 3px; }

  /* company name */
  .wordmark {
    position: absolute; color: var(--brand-blue);
    font-family: "PT Sans", sans-serif; font-weight: 400; line-height: 1;
  }
  .wordmark--small { right: 16px; bottom: 58px; font-size: 32px; }
  .wordmark--large { right: 24px; top: 302px; font-size: 54px; }

  /* slide heading */
  .slide-heading { position: absolute; left: 0; top: 12px; height: 32px; display: flex; align-items: center; }
  .heading-flag { width: 22px; height: 32px; }
  .heading-title { margin-left: 8px; color: var(--title-blue); font-weight: 700; font-size: 25px; }

  /* cover */
  .cover-band {
    position: absolute; left: 0; top: 0; width: 100%; height: 257px;
    background: linear-gradient(180deg, var(--band-top), var(--band-bottom));
    border-bottom: 5px solid #15202e;
  }
  .cover-title {
    position: absolute; right: 34px; top: 94px; color: var(--white);
    font-weight: 700; font-size: 35px; line-height: 1.1; white-space: nowrap;
  }
  .cover-subtext {
    position: absolute; right: 34px; top: 140px; text-align: right; white-space: nowrap;
    color: var(--white); font-size: 13.5px; line-height: 20px;
  }
  .portrait-ring {
    position: absolute; left: 20px; top: 170px; width: 210px; height: 210px; border-radius: 50%;
    background: #1a1f26; padding: 7px;
  }
  .portrait-ring-inner { width: 100%; height: 100%; border-radius: 50%; background: var(--brand-blue); padding: 4px; }
  .portrait {
    width: 100%; height: 100%; border-radius: 50%;
    background: linear-gradient(180deg, #eef1f4 0%, #c9b2a2 50%, #3a3f48 100%);
  }

  /* lists */
  .section-title { position: absolute; left: 43px; top: 70px; color: var(--title-blue); font-weight: 700; font-size: 17px; }
  .check-list {
    position: absolute; left: 46px; top: 100px; list-style: none;
    color: var(--body-ink); font-size: 12.6px; line-height: 19px; white-space: nowrap;
  }
  .check-list li { position: relative; padding-left: 20px; }
  .check-list li::before {
    content: ""; position: absolute; left: 0; top: 4px; width: 11px; height: 11px;
    border: 1.5px solid var(--tick-ink); background: var(--white);
  }
  .check-list li::after {
    content: ""; position: absolute; left: 4px; top: 0; width: 5px; height: 11px;
    border-right: 2.5px solid var(--tick-ink); border-bottom: 2.5px solid var(--tick-ink); transform: rotate(40deg);
  }
  .team-photo {
    position: absolute; left: 205px; top: 92px; width: 360px; height: 280px;
    background: linear-gradient(180deg, rgba(225,235,243,0) 0%, rgba(95,105,125,0.45) 18%, rgba(85,92,108,0.45) 55%, rgba(200,215,225,0.3) 82%, rgba(230,242,248,0) 100%);
  }
</style>
</head>
<body>
<main class="canvas">

  <section class="slide slide--cover">
    <div class="cover-band"></div>
    <h1 class="cover-title">Project Title Here</h1>
    <p class="cover-subtext">Subtext here Subtext here Subtext here Subtext here Subtext here<br>Subtext here Subtext here Subtext here</p>
    <div class="portrait-ring">
      <div class="portrait-ring-inner">
        <div class="portrait" role="img" aria-label="Portrait photo of the presenter"></div>
      </div>
    </div>
    <div class="wordmark wordmark--large">Vantora</div>
    <footer class="footer-bar">
      <span class="slide-number">01</span>
      <span class="footer-text footer-text--date">01/02/15</span>
      <span class="nav-button nav-button--start">Start</span>
    </footer>
  </section>

  <section class="slide slide--outline">
    <header class="slide-heading">
      <svg class="heading-flag" viewBox="0 0 22 32"><polygon points="0,0 22,0 22,32 0,32 8,16" fill="#0056a2"/></svg>
      <h2 class="heading-title">Presentation Outline</h2>
    </header>
    <div class="wordmark wordmark--small">Vantora</div>
    <footer class="footer-bar">
      <span class="slide-number">02</span>
      <span class="footer-text">tagline/slogan about your company</span>
      <div class="nav"><span class="nav-button nav-button--back">Back</span><span class="nav-button nav-button--next">Next</span></div>
    </footer>
  </section>

  <section class="slide slide--about">
    <header class="slide-heading">
      <svg class="heading-flag" viewBox="0 0 22 32"><polygon points="0,0 22,0 22,32 0,32 8,16" fill="#0056a2"/></svg>
      <h2 class="heading-title">Presentation Outline</h2>
    </header>
    <h3 class="section-title">Something About Your Business</h3>
    <ul class="check-list">
      <li>Melbourne based management consulting organisation</li>
      <li>Partnering with clients to lead strategic process and system improvement</li>
      <li>Focus on clear and focused execution and enablement of change</li>
      <li>“Hands On and Coaching” approach to every engagement</li>
      <li>Advisory in Project, Process and Change Management, Business Analysis and BI</li>
      <li>Extensive experience across a wide range of industries and sectors</li>
      <li>Clean, practical and proven delivery methodologies</li>
      <li>A team constantly looking into the latest methods, tools, and technology to better<br>build our clients’ capabilities and ensure ongoing success in project delivery,<br>all while embracing tried and true best practice approaches as well</li>
      <li>Specialists in the accounting, legal, financial services and health sectors</li>
      <li>Not Just Projects! We help the middle market navigate<br>transformational change through and through.</li>
    </ul>
    <div class="wordmark wordmark--small">Vantora</div>
    <footer class="footer-bar">
      <span class="slide-number">03</span>
      <span class="footer-text">tagline/slogan about your company</span>
      <div class="nav"><span class="nav-button nav-button--back">Back</span><span class="nav-button nav-button--next">Next</span></div>
    </footer>
  </section>

  <section class="slide slide--services">
    <header class="slide-heading">
      <svg class="heading-flag" viewBox="0 0 22 32"><polygon points="0,0 22,0 22,32 0,32 8,16" fill="#0056a2"/></svg>
      <h2 class="heading-title">Presentation Outline</h2>
    </header>
    <h3 class="section-title">Our Services</h3>
    <div class="team-photo" role="img" aria-label="Photo of a group of business professionals standing together"></div>
    <ul class="check-list">
      <li>Strategy</li>
      <li>Project Delivery</li>
      <li>Coaching</li>
      <li>PMO Setup</li>
      <li>Governance</li>
      <li>Reporting</li>
      <li>Process Mapping</li>
      <li>Change Plans</li>
      <li>Business Analysis Services</li>
      <li>Workshops</li>
      <li>System Selection</li>
      <li>Data Insights</li>
    </ul>
    <div class="wordmark wordmark--small">Vantora</div>
    <footer class="footer-bar">
      <span class="slide-number">04</span>
      <span class="footer-text">tagline/slogan about your company</span>
      <div class="nav"><span class="nav-button nav-button--back">Back</span><span class="nav-button nav-button--next">Next</span></div>
    </footer>
  </section>

</main>
</body>
</html>
```